New Bicycle shop business card

Hi!
I'm looking for a business card for my new proffesional bike mechanics shop. This shop is only for fixing broken bikes and not selling bikes.
Peferbly a modern and sleek and modern design.
Colors: black, grey, red, white
Information:
Name: Velowerkplaats Martens
Shop owner: Bart Martens & Sofie Vanhulle
Website: www.velowerkplaats-martens.be
Email: info@velowerkplaats-martens.be
Phone number: +32471936208
Street adres: Molenweg 57
9470 Heidebeke
Slogan/shop information: Herstellingen van alle merken.
Logo: see files.
Target Market(s)
People who seek a mechanic to fix or upgrade their bikes.
Contact Information for Business Card
Information:
Website: info@velowerkplaats-martens.be
9470 Heidebeke
Logo: see files.

```html
<!DOCTYPE html>
<html lang="nl">
<head>
<meta charset="utf-8">
<title>Velowerkplaats Martens – Visitekaartje</title>
<link rel="stylesheet" href="https://fonts.googleapis.com/css2?family=Montserrat:wght@800&family=Open+Sans:wght@400;700&display=swap">
<style>
  :root {
    --page: #e4e4e6;
    --card-black: #111112;
    --card-white: #ffffff;
    --ink: #141414;
    --grey: #555558;
    --red: #d9465c;
    --white: #ffffff;
  }
  * { box-sizing: border-box; margin: 0; padding: 0; }
  html, body { width: 1200px; height: 900px; overflow: hidden; }
  body {
    background: var(--page);
    font-family: "Open Sans", Arial, sans-serif;
    display: flex;
    flex-direction: column;
    align-items: center;
    justify-content: center;
    gap: 40px;
  }
  .card {
    width: 620px;
    height: 400px;
    border-radius: 4px;
    position: relative;
    overflow: hidden;
    box-shadow: 0 6px 18px rgba(0,0,0,.18);
  }

  /* Front */
  .card--front {
    background: var(--card-black);
    display: flex;
    align-items: center;
    justify-content: center;
  }
  .front__mark {
    display: flex;
    flex-direction: column;
    align-items: center;
    gap: 22px;
  }
  .wordmark__square {
    width: 52px; height: 52px;
    background: var(--red);
  }
  .wordmark__name {
    font-family: "Montserrat", Arial, sans-serif;
    font-weight: 800;
    letter-spacing: 1.5px;
    text-transform: uppercase;
  }
  .card--front .wordmark__name {
    color: var(--white);
    font-size: 32px;
    line-height: 1.2;
    text-align: center;
    letter-spacing: 3px;
  }

  /* Back */
  .card--back { background: var(--card-white); }
  .back__brand {
    position: absolute;
    left: 44px; top: 58px;
  }
  .wordmark {
    display: flex;
    align-items: center;
    gap: 12px;
  }
  .wordmark__circle {
    width: 30px; height: 30px; border-radius: 50%;
    background: var(--red);
    flex: none;
  }
  .card--back .wordmark__name { color: var(--ink); font-size: 19px; }
  .tagline {
    margin: 4px 0 0 42px;
    font-size: 12px;
    color: var(--ink);
  }
  .back__person {
    position: absolute;
    left: 44px; top: 190px;
  }
  .person__names {
    color: var(--red);
    font-weight: 700;
    font-size: 17px;
    text-transform: uppercase;
    letter-spacing: .3px;
  }
  .person__role { color: var(--grey); font-size: 13px; margin-top: 2px; }
  .contact {
    position: absolute;
    left: 44px; top: 268px;
    list-style: none;
    font-size: 13px;
    color: var(--grey);
    line-height: 23px;
  }
  .contact li { display: flex; align-items: center; gap: 10px; }
  .contact svg { width: 14px; height: 14px; fill: var(--red); flex: none; }
  .contact .contact__address { padding-left: 24px; }
</style>
</head>
<body>

<section class="card card--front" aria-label="Voorkant visitekaartje">
  <div class="front__mark">
    <span class="wordmark__square"></span>
    <span class="wordmark__name">Velowerkplaats<br>Martens</span>
  </div>
</section>

<section class="card card--back" aria-label="Achterkant visitekaartje">
  <div class="back__brand">
    <div class="wordmark">
      <span class="wordmark__circle"></span>
      <span class="wordmark__name">Velowerkplaats Martens</span>
    </div>
    <p class="tagline">Herstellingen van alle merken</p>
  </div>

  <div class="back__person">
    <p class="person__names">Bart Martens &amp; Sofie Vanhulle</p>
    <p class="person__role">Shop owner</p>
  </div>

  <ul class="contact">
    <li>
      <svg viewBox="0 0 24 24" aria-hidden="true"><path d="M6.6 10.8a15.1 15.1 0 0 0 6.6 6.6l2.2-2.2a1 1 0 0 1 1-.25 11.4 11.4 0 0 0 3.6.57 1 1 0 0 1 1 1V20a1 1 0 0 1-1 1A17 17 0 0 1 3 4a1 1 0 0 1 1-1h3.5a1 1 0 0 1 1 1c0 1.25.2 2.45.57 3.57a1 1 0 0 1-.25 1z"/></svg>
      +32471936208
    </li>
    <li>
      <svg viewBox="0 0 24 24" aria-hidden="true"><path d="M2 5h20v14H2z"/><path d="M3 6l9 7 9-7" stroke="#fff" stroke-width="1.6" fill="none"/></svg>
      info@velowerkplaats-martens.be
    </li>
    <li>
      <svg viewBox="0 0 24 24" aria-hidden="true"><circle cx="12" cy="12" r="10"/><path d="M2 12h20M12 2c3 3 3 17 0 20M12 2c-3 3-3 17 0 20" stroke="#fff" stroke-width="1.4" fill="none"/></svg>
      www.velowerkplaats-martens.be
    </li>
    <li class="contact__address">Molenweg 57, 9470 Heidebeke</li>
  </ul>
</section>

</body>
</html>
```